Business Cards for IT Consulting Company (Managed Service Provider)

I am looking to have some business cards printed and would like some designs. We are an IT Consulting company based in Vancouver BC. I would like a nice clean and modern look to the cards. I have uploaded all the versions of my logo so parts can be used as needed. Here is a snippit from our website homepage:

Kelbrook Systems Ltd. is an IT Solutions Partner located in Vancouver BC, Canada. We offer IT solutions and support to customers in the greater Vancouver Area. With expertise in Microsoft platforms, as well as Linux and Mac OSX and over 12 years experience in the IT industry, Kelbrook Systems is dedicated to offering our clients top quality service and products. We take pride in the solutions we offer our customers. The greatest compliment a client can give us is to recommend our services.

Kelbrook Systems Ltd. offers a wide range of IT services from onsite service to remote support and managed service solutions. This allows clients to choose the support path that best suits their company’s needs. Supporting many different sized companies from small to enterprise level over the past 12 years Kelbrook Systems has the experience and expertise needed to ensure things run smoothly. Allowing our clients to focus on doing business.

Revolutionizing the way IT services are delivered.

Kelbrook Systems is dedicated to providing our clients with IT solutions that work and grow with them for years to come. This philosophy helps save money in the long run instead of replacing equipment constantly. Far too often IT solutions are not well thought out and while possibly solving the problem at hand, require replacement due to growth or quality within a very short time frame. Kelbrook Systems takes pride in providing solutions that will last and be able to accommodate growth without the need for replacement.

Industry/Entity Type

Information Technology

Contact Information for Business Card

Kelbrook Systems Ltd.
(Employee Name)
Eml: (Employees Email Address)
Web: kelbrook.me
Ph: 604-555-0142

Font styles to use
Serif
Sans Serif

Requirements
Must have
• The Company logo and company colors.
Nice to have
• - Our tag line: "Revolutionizing IT Services" or "Revolutionizing the way IT services are delivered."
• - Also I really like the idea of nature and technology together blending which is sort of where my logo came from so integrating that somehow onto the business cards would be great.

```html
<!DOCTYPE html>
<html lang="en">
<head>
<meta charset="utf-8">
<title>Kelbrook Systems Ltd. — Business Cards</title>
<link href="https://fonts.googleapis.com/css2?family=Open+Sans:wght@400;600;700&family=Questrial&display=swap" rel="stylesheet">
<style>
  :root {
    --backdrop: #d4d4d4;
    --card-white: #f1f1f1;
    --divider: #e2e2e2;
    --panel-grey: #5d5d5d;
    --brand-blue: #0a8fd3;
    --text-grey: #5a5a5a;
    --contact-white: #f4f4f4;
    --city-dark: #2b3138;
    --city-warm: #a86a2c;
    --city-teal: #3d6a6e;
  }
  * { box-sizing: border-box; margin: 0; padding: 0; }
  html, body {
    width: 1200px; height: 754px; overflow: hidden;
    background: var(--backdrop);
  }
  .sheet { position: relative; width: 1200px; height: 754px; }

  .card {
    position: absolute; top: 242px;
    width: 459px; height: 255px;
    background: var(--card-white);
    overflow: hidden;
  }
  .card--front { left: 120px; }
  .card--back { left: 624px; }

  .wordmark {
    position: absolute;
    display: flex; align-items: center; gap: 8px;
    font-family: "Open Sans", sans-serif;
    font-weight: 600; font-size: 19px;
    color: var(--brand-blue);
    letter-spacing: 0.2px;
    white-space: nowrap;
  }
  .wordmark__square {
    width: 16px; height: 16px;
    background: var(--brand-blue);
  }
  .card--front .wordmark { right: 22px; top: 48px; }
  .card--back .wordmark { left: 30px; top: 50px; }

  /* front */
  .holder { position: absolute; left: 33px; top: 58px; }
  .holder__name {
    font-family: "Open Sans", sans-serif; font-weight: 700;
    font-size: 14.5px; color: var(--brand-blue); letter-spacing: 0.3px;
    text-transform: uppercase; line-height: 1;
  }
  .holder__title {
    margin-top: 4px;
    font-family: "Questrial", sans-serif; font-size: 11.5px; color: var(--text-grey);
  }
  .divider {
    position: absolute; left: 0; top: 115px; width: 100%; height: 5px;
    background: var(--divider);
  }
  .contact-panel {
    position: absolute; left: 0; top: 120px; width: 100%; height: 112px;
    background: var(--panel-grey);
  }
  .contact-panel__notch {
    position: absolute; left: 38px; top: -1px;
    width: 0; height: 0;
    border-left: 4px solid transparent; border-right: 4px solid transparent;
    border-top: 5px solid var(--divider);
  }
  .contact-list { position: absolute; left: 33px; top: 32px; list-style: none; }
  .contact-list li {
    display: flex; align-items: center; gap: 7px;
    height: 16.5px;
    font-family: "Questrial", sans-serif; font-size: 12.5px;
    color: var(--contact-white);
  }
  .contact-list svg { width: 12px; height: 12px; flex: none; }
  .brand-band {
    position: absolute; left: 0; bottom: 0; width: 100%; height: 23px;
    background: var(--brand-blue);
  }

  /* back */
  .city-photo {
    position: absolute; left: 0; top: 122px; width: 100%; height: 113px;
    background:
      radial-gradient(ellipse at 30% 70%, rgba(214,140,58,0.55), transparent 55%),
      radial-gradient(ellipse at 75% 40%, rgba(200,120,50,0.45), transparent 50%),
      linear-gradient(135deg, var(--city-teal), var(--city-dark) 45%, var(--city-warm) 100%);
  }
  .card--back .brand-band { height: 20px; }
</style>
</head>
<body>
<main class="sheet">

  <section class="card card--front" aria-label="Business card front">
    <div class="holder">
      <p class="holder__name">Jordan Ellery</p>
      <p class="holder__title">General Manager</p>
    </div>
    <div class="wordmark"><span class="wordmark__square"></span>Kelbrook Systems Ltd.</div>
    <div class="divider"></div>
    <div class="contact-panel">
      <span class="contact-panel__notch"></span>
      <ul class="contact-list">
        <li>
          <svg viewBox="0 0 12 12" aria-hidden="true"><rect width="12" height="12" rx="2" fill="#0a8fd3"/><path d="M3.6 2.6l1.3 0.2 0.5 1.6-0.8 0.6c0.4 0.9 1.1 1.6 2 2l0.6-0.8 1.6 0.5 0.2 1.3c-0.4 0.6-1 0.8-1.6 0.6C5.4 8.1 3.9 6.6 3.4 4.6 3.2 3.9 3.1 3.1 3.6 2.6z" fill="#fff"/></svg>
          604-555-0142
        </li>
        <li>
          <svg viewBox="0 0 12 12" aria-hidden="true"><rect width="12" height="12" rx="2" fill="#0a8fd3"/><rect x="2.5" y="3.5" width="7" height="5" fill="none" stroke="#fff" stroke-width="0.9"/><path d="M2.5 3.5L6 6.3 9.5 3.5" fill="none" stroke="#fff" stroke-width="0.9"/></svg>
          info@kelbrook.me
        </li>
        <li>
          <svg viewBox="0 0 12 12" aria-hidden="true"><rect width="12" height="12" rx="2" fill="#0a8fd3"/><circle cx="6" cy="6" r="3.6" fill="none" stroke="#fff" stroke-width="0.8"/><ellipse cx="6" cy="6" rx="1.5" ry="3.6" fill="none" stroke="#fff" stroke-width="0.7"/><path d="M2.4 6h7.2" stroke="#fff" stroke-width="0.7"/></svg>
          www.kelbrook.me
        </li>
      </ul>
    </div>
    <div class="brand-band"></div>
  </section>

  <section class="card card--back" aria-label="Business card back">
    <div class="wordmark"><span class="wordmark__square"></span>Kelbrook Systems Ltd.</div>
    <div class="city-photo" role="img" aria-label="Aerial night view of downtown city towers with warm glowing streets"></div>
    <div class="brand-band"></div>
  </section>

</main>
</body>
</html>
```